VistaLume webpage - Design only no coding required

Please refer to "web content" uploaded 23rd Sep for content

We are a digital signage company based in Jakarta, Indonesia.

Our core business is placement of LCD Tv's in waiting rooms of various hospitals in Indonesia which plays educational videos regarding various health topics (prescription/ethical medicines), OTC drugs TVC and other FMCG and ads.

Our client portfolio consists of the worlds biggest and well known Pharmaceutical companies and also local pharmaceutical companies.

Other parts of our business are as follows:
- Patient symposiums
- Booths for product activation
- Queuing systems that we have developed in house that use an android tablet and connect to our TV's
- Branding. eg. Lift doors, banners (static signage)
- Hospital management software. Specially developed software that comes in a generic format and needs to be customized to suit each hospital. It manages everything for phone/web booking, queues, registration, patient records, doctors schedules, referrals, pharmacy and inventory and checkout/payments.

We are after a website redesign that is visually attractive and modern as we also deal with many advertising agencies.

Our logo is orange and black, however the black & white can be reversed if necessary.

Pages will need to be available in English & Bahasa Indonesia language formats.

I am happy to answer any questions asap, i can be contacted at info@vistalume.example.id

current site (www.vistalume.example.id)

Target Market(s)

Mainly our business is B2B dealing with advertising clients either directly or through ad agencies.

The other aspect of our target market is hospitals where we place our screens.

There is (but not largely) and consumer audience.

In summary:
We have the following target markets:
1. Advertisers/ad agencies
2. Hospitals that wish to use our business model to display content to their patients 3. We are in a developing country however most of our viewers and clients are from a high demographic profile

Industry/Entity Type

Pharmaceutical

Requirements
Must have
• We will require duplicates of the pages in English & Bahasa Indonesia

I would like the initial designs with a focus on being clean yet bold and emphasis on typography.

The following pages will be required (but not limited to) to qualify for the prize:

-Home

- About Us

- Services
(sub pages)
=Digital Signage
=Video Content Production
=Hospital Branding
=Event Management
=Seminar
=Queue System
=Hospital Management Software

-Why Choose Us?

- Contact Us

- Clients & Partners

- Gallery

Based on the "Nice to haves" site examples we do not necessarily require pictures of our LCD's/content on the main page(s) and would be happy to purchase required stock photos if needed/agreed.

We definitely want a modern feel and do not wish to overload with too much info on the main page.

(Please note the text in the attached file will most likely be changed once we have a design concept, probably less text)

Webpages we like:
http://www.brinklanternstudio.example/
http://quillharbor.example

Nice to have
• This is some of the international players which we want our site to look like:
www.pardelsign.example.au
http://www.morvexpanel.example.uk/
www.tallowgrid.example/

Should not have
• We prefer not to have old outdated fonts and a website that resembles anything like the current one, we are after a modern and professional feel.
These are some of our relative competitors of which we DO NOT want our website looking like but as a reference:
http://curabyte-global.example/index.html
http://zrk.example.id/

```html
<!DOCTYPE html>
<html lang="en">
<head>
<meta charset="utf-8">
<title>VistaLume — Digital Signage</title>
<link rel="stylesheet" href="https://fonts.googleapis.com/css2?family=Source+Sans+3:wght@300;400;600;700&display=swap">
<style>
:root{
  --orange:#e05a0c;
  --black:#050505;
  --ink:#2d2d2d;
  --text:#4a4a4a;
  --muted:#8a8a8a;
  --band:#f2f2f2;
  --line:#d6d6d6;
  --white:#ffffff;
}
*{box-sizing:border-box;margin:0;padding:0}
html,body{width:1200px;height:2233px;overflow:hidden}
body{position:relative;background:var(--white);font-family:"Source Sans 3",Arial,sans-serif;color:var(--text)}

/* Header */
.site-header{position:absolute;left:0;top:0;width:1200px;height:127px;background:var(--black)}
.brand{position:absolute;left:92px;top:54px;display:flex;align-items:center;gap:14px}
.brand-mark{width:58px;height:58px;background:var(--orange)}
.brand-name{font-size:40px;font-weight:700;color:var(--white);letter-spacing:.3px}
.main-nav{position:absolute;right:85px;top:75px;display:flex;gap:24px}
.main-nav a{color:var(--white);text-decoration:none;font-size:16px;font-weight:400;letter-spacing:.2px}

/* Hero */
.hero{position:absolute;left:0;top:127px;width:1200px;height:458px;
  background:linear-gradient(100deg,#c9d3d8 0%,#a8b9c1 30%,#6f7d85 50%,#b4c3ca 70%,#8e9ea6 100%)}
.hero-arrow{position:absolute;top:205px;width:54px;height:54px;border-radius:50%;background:rgba(70,70,70,.55);display:flex;align-items:center;justify-content:center}
.hero-arrow.prev{left:88px}
.hero-arrow.next{left:1060px}
.hero-caption{position:absolute;left:185px;background:rgba(55,55,55,.78);color:var(--white);font-size:21px;font-weight:600;letter-spacing:.4px;padding:0 15px;line-height:52px;height:52px;white-space:nowrap}
.hero-caption.one{top:263px;width:434px}
.hero-caption.two{top:329px;width:411px;height:50px;line-height:50px}

/* Section titles */
.section-title{position:absolute;left:0;width:1200px;text-align:center;font-size:31px;font-weight:400;color:var(--ink);letter-spacing:.5px;line-height:38px}
.title-rule{position:absolute;left:555px;width:90px;height:3px;background:var(--orange)}

/* About */
.about-photo{position:absolute;left:119px;top:692px;width:344px;height:230px;background:linear-gradient(135deg,#3a4148 0%,#1b1f24 60%,#2c3238 100%)}
.about-heading{position:absolute;left:517px;top:685px;font-size:19px;font-weight:400;color:var(--ink);letter-spacing:.2px}
.about-copy{position:absolute;left:517px;top:722px;width:575px;font-size:14px;line-height:24px;color:var(--text)}
.about-list{position:absolute;left:517px;top:809px;list-style:none}
.about-list li{display:flex;align-items:center;gap:17px;height:32.3px;font-size:14px;color:var(--text)}

/* Services */
.services-band{position:absolute;left:0;top:977px;width:1200px;height:464px;background:var(--band)}
.services-intro{position:absolute;left:100px;top:1068px;width:1000px;text-align:center;font-size:14px;line-height:23px;color:var(--text)}
.service{position:absolute;display:flex;gap:23px}
.service-icon{width:67px;height:60px;background:var(--orange);display:flex;align-items:center;justify-content:center;flex:none}
.service-name{font-size:21px;color:var(--ink);line-height:24px;margin-top:3px;white-space:nowrap}
.service-text{font-size:14px;color:var(--muted);margin-top:4px;white-space:nowrap}

/* Gallery */
.gallery-tabs{position:absolute;top:1559px;left:0;width:1200px;height:42px}
.tab{position:absolute;top:0;height:42px;border:1px solid var(--line);background:var(--white);font-size:17px;color:var(--ink);display:flex;align-items:center;justify-content:center}
.tab.active{border-color:var(--orange)}
.gallery-item{position:absolute;top:1648px;width:221px}
.gallery-media{height:172px}
.gallery-caption{height:68px;background:var(--orange);color:var(--white);padding:14px 14px 0}
.gallery-caption strong{display:block;font-size:15px;font-weight:400;letter-spacing:.3px}
.gallery-caption span{display:block;font-size:13px;margin-top:4px}
.divider-shadow{position:absolute;left:250px;top:1930px;width:700px;height:14px;border-radius:50%;box-shadow:0 10px 14px -6px rgba(0,0,0,.18)}

/* Clients */
.client{position:absolute;top:1977px;width:141px;height:111px;border:1px solid var(--line);background:var(--white);display:flex;align-items:center;justify-content:center;text-align:center;font-size:15px;font-weight:600;color:#3d4f7a;line-height:18px;padding:0 8px}

/* Footer */
.site-footer{position:absolute;left:0;top:2132px;width:1200px;height:101px;background:var(--black)}
.footer-links{position:absolute;left:86px;top:26px;font-size:13.5px;color:var(--white)}
.footer-copy{position:absolute;left:86px;top:60px;font-size:12.5px;color:var(--white)}
.social{position:absolute;top:30px;width:36px;height:36px}
</style>
</head>
<body>

<header class="site-header">
  <div class="brand"><span class="brand-mark"></span><span class="brand-name">VistaLume</span></div>
  <nav class="main-nav">
    <a href="#">HOME</a><a href="#">ABOUT US</a><a href="#">SERVICES</a><a href="#">WHY CHOOSE US?</a><a href="#">CONTACT US</a><a href="#">GALLERY</a>
  </nav>
</header>

<section class="hero" role="img" aria-label="Blurred photo of business people talking in a bright office with large windows">
  <span class="hero-arrow prev"><svg width="16" height="24" viewBox="0 0 16 24"><path d="M12 2 3 12l9 10" fill="none" stroke="#fff" stroke-width="1.6"/></svg></span>
  <span class="hero-arrow next"><svg width="16" height="24" viewBox="0 0 16 24"><path d="m4 2 9 10-9 10" fill="none" stroke="#fff" stroke-width="1.6"/></svg></span>
  <div class="hero-caption one">INDEPENDENT ENTERTAINMENT COMPANY</div>
  <div class="hero-caption two">VIVAMUS SUSCIPIT TORTOR EGET FELIS</div>
</section>

<h2 class="section-title" style="top:603px">ABOUT US</h2>
<span class="title-rule" style="top:645px"></span>
<div class="about-photo" role="img" aria-label="Photo of a man in a shirt and tie touching a floating screen interface"></div>
<h3 class="about-heading">VISTALUME IS AN ADVERTISING DIGITAL SYSTEM</h3>
<p class="about-copy">Maecenas ligula urna placerat in lectus pulvinar pellentesque rutr turpis. Aenean in magn aliquet eleifend quam eget rutrum massa. Aliquam faucibus fauicibus venenatis integer ti ncidunt. Etam cursus lectus nec tortor sagittis, at ultrices diam tempus.</p>
<ul class="about-list">
  <li><svg width="14" height="14" viewBox="0 0 14 14"><circle cx="7" cy="7" r="7" fill="#e05a0c"/><path d="M4 7h6M7 4l3 3-3 3" fill="none" stroke="#fff" stroke-width="1.6"/></svg>Donec placerat aliquam leo donec sapien.</li>
  <li><svg width="14" height="14" viewBox="0 0 14 14"><circle cx="7" cy="7" r="7" fill="#e05a0c"/><path d="M4 7h6M7 4l3 3-3 3" fill="none" stroke="#fff" stroke-width="1.6"/></svg>Morbi arcu lacus iaculis sit amet libero eu vul.</li>
  <li><svg width="14" height="14" viewBox="0 0 14 14"><circle cx="7" cy="7" r="7" fill="#e05a0c"/><path d="M4 7h6M7 4l3 3-3 3" fill="none" stroke="#fff" stroke-width="1.6"/></svg>Fusce dignissim enim vel pretium vulputate jus.</li>
  <li><svg width="14" height="14" viewBox="0 0 14 14"><circle cx="7" cy="7" r="7" fill="#e05a0c"/><path d="M4 7h6M7 4l3 3-3 3" fill="none" stroke="#fff" stroke-width="1.6"/></svg>Aenean fringilla mauris a nisi aliquet ut congue.</li>
</ul>

<section class="services-band">
  <h2 class="section-title" style="top:22px">SERVICES</h2>
  <span class="title-rule" style="top:66px"></span>
</section>
<p class="services-intro">Vivamus sagittis lacus vel augue laoreet rutrum faucibus dolor auctor. Aenean lacinia bibendum nulla sed consectetur. Because we think it's time for a new exciting challenge! Are you ready for an adventure to remember for a lifetime? Accusantium quam, ultricies eget tempor id, aliquam eget nibihe</p>

<div class="service" style="left:234px;top:1150px">
  <span class="service-icon"><svg width="34" height="30" viewBox="0 0 34 30" fill="none" stroke="#fff" stroke-width="2"><path d="M17 3 31 10 17 17 3 10Z"/><path d="M3 15l14 7 14-7M3 20l14 7 14-7"/></svg></span>
  <div><div class="service-name">Digital Signage</div><div class="service-text">Etam cursus lectus nec tortor sagitt</div></div>
</div>
<div class="service" style="left:651px;top:1150px">
  <span class="service-icon"><svg width="34" height="30" viewBox="0 0 34 30" fill="none" stroke="#fff" stroke-width="2"><path d="M31 3 4 14l10 3 3 10Z"/><path d="M14 17 31 3"/></svg></span>
  <div><div class="service-name">Event Management</div><div class="service-text">Etam cursus lectus nec tortor sagitt</div></div>
</div>
<div class="service" style="left:234px;top:1240px">
  <span class="service-icon"><svg width="34" height="32" viewBox="0 0 34 32"><path d="M17 3 30 9v14l-13 7-13-7V9Z" fill="#fff"/><path d="M4 9l13 7 13-7M17 16v14" fill="none" stroke="#e05a0c" stroke-width="1.6"/></svg></span>
  <div><div class="service-name">Video Content Production</div><div class="service-text">Etam cursus lectus nec tortor sagitt</div></div>
</div>
<div class="service" style="left:651px;top:1240px">
  <span class="service-icon"><svg width="34" height="32" viewBox="0 0 34 32" fill="none" stroke="#fff" stroke-width="2"><path d="M8 5h14l5 4v18H8Z"/><path d="M22 5v4h5M13 13h9M13 18h9M13 23h6"/></svg></span>
  <div><div class="service-name">Seminar</div><div class="service-text">Etam cursus lectus nec tortor sagitt</div></div>
</div>
<div class="service" style="left:234px;top:1333px">
  <span class="service-icon"><svg width="34" height="34" viewBox="0 0 34 34" fill="#fff"><path d="M14 5h6l1 4 3 1.5 3.5-2 4 4-2 3.5L31 19l-4 1-1 3 2 3.5-4 4-3.5-2L17 30l-1 4h-4l-1-4-3-1.5-3.5 2-4-4 2-3.5L2 20l-1-5 4-1 1.5-3-2-3.5 4-4 3.5 2L14 5Z" transform="scale(.85) translate(3 0)"/><circle cx="16" cy="17" r="5" fill="#e05a0c"/></svg></span>
  <div><div class="service-name">Hospital Branding</div><div class="service-text">Etam cursus lectus nec tortor sagitt</div></div>
</div>
<div class="service" style="left:651px;top:1333px">
  <span class="service-icon"><svg width="34" height="34" viewBox="0 0 34 34" fill="none" stroke="#fff" stroke-width="2"><path d="M13 4h10M15 4v10L6 29h22L19 14V4"/><path d="M10 22h14"/></svg></span>
  <div><div class="service-name">Queue System</div><div class="service-text">Etam cursus lectus nec tortor sagitt</div></div>
</div>

<h2 class="section-title" style="top:1466px">GALLERY</h2>
<span class="title-rule" style="top:1507px"></span>
<div class="gallery-tabs">
  <span class="tab active" style="left:329px;width:102px">IMAGES</span>
  <span class="tab" style="left:465px;width:108px">EXAMPLE</span>
  <span class="tab" style="left:606px;width:110px">VIDEOS</span>
  <span class="tab" style="left:746px;width:126px">ALL ITEMS</span>
</div>

<div class="gallery-item" style="left:91px">
  <div class="gallery-media" role="img" aria-label="Blue digital medical emblem with light rays" style="background:radial-gradient(circle at 50% 45%,#cfe6ff 0%,#3a86d0 40%,#0b2c5a 100%)"></div>
  <div class="gallery-caption"><strong>SAMPLE IMAGE I</strong><span>Ut id tincidunt lorem</span></div>
</div>
<div class="gallery-item" style="left:357px">
  <div class="gallery-media" role="img" aria-label="Network of glowing icons on a dark blue background" style="background:linear-gradient(135deg,#0e2a4d 0%,#1f5e9c 55%,#0a1c36 100%)"></div>
  <div class="gallery-caption"><strong>SAMPLE IMAGE I</strong><span>Ut id tincidunt lorem</span></div>
</div>
<div class="gallery-item" style="left:624px">
  <div class="gallery-media" role="img" aria-label="Calendar page with a deadline circled by a pen" style="background:linear-gradient(160deg,#f4f6f8 0%,#dde3e8 60%,#b9c3cc 100%)"></div>
  <div class="gallery-caption"><strong>SAMPLE IMAGE I</strong><span>Ut id tincidunt lorem</span></div>
</div>
<div class="gallery-item" style="left:892px">
  <div class="gallery-media" role="img" aria-label="Business team meeting in a conference room" style="background:linear-gradient(135deg,#e7dccd 0%,#b99c7e 50%,#6f6258 100%)"></div>
  <div class="gallery-caption"><strong>SAMPLE IMAGE I</strong><span>Ut id tincidunt lorem</span></div>
</div>

<span class="divider-shadow"></span>

<div class="client" style="left:134px">Wrenfield</div>
<div class="client" style="left:325px">Orvane Assurance Group</div>
<div class="client" style="left:518px">Pellmar Mkt.</div>
<div class="client" style="left:707px">Kestrin Biotech</div>
<div class="client" style="left:893px">Brisk Fern Tech</div>

<footer class="site-footer">
  <p class="footer-links">Home | About Us | Services | Why Choose Us? | Contact Us | Gallery</p>
  <p class="footer-copy">Copyrights 2013. All Rights Reserved.</p>
  <span class="social" style="left:895px;background:#3b5ea8"></span>
  <span class="social" style="left:945px;background:#2ba6de"></span>
  <span class="social" style="left:995px;background:#f26a1b"></span>
  <span class="social" style="left:1042px;background:#d9262b"></span>
</footer>

</body>
</html>
```